Home page redesign for an international job board

Need a modern design based on current structure of the page. I am happy with the current structure and layout/architecture, not entirely happy with how it looks. While I still want to keep most of the elements in place ( especially the search box) I would like to get another look and feel - more appealing to any audience related to online job search

Home page is: www.lucrubrisa.ro

Target Market(s)

job seeekers and employers

Industry/Entity Type

Architecture

Number of Pages Required

1 page

Font styles to use
Sans Serif

Colors
33a6d7

Requirements
Must have
• Stay with the same structure: Seach box, latest jobs, articles
Nice to have
• Key element: search for jobs - this needs to be very clear

```html
<!DOCTYPE html>
<html lang="en">
<head>
<meta charset="utf-8">
<title>LucruBrisa – Home</title>
<link href="https://fonts.googleapis.com/css2?family=Open+Sans:wght@400;600;700&family=Raleway:wght@500;600;700&display=swap" rel="stylesheet">
<style>
:root{
  --accent:#33a6d7;
  --accent-dark:#1f86b3;
  --black:#050505;
  --ink:#1a1a1a;
  --grey:#3b3b3b;
  --panel:rgba(150,150,150,.55);
  --white:#ffffff;
}
*{box-sizing:border-box;margin:0;padding:0}
html,body{width:1200px;height:2362px;overflow:hidden}
body{position:relative;background:var(--grey);font-family:"Open Sans",Arial,sans-serif;color:var(--white)}
.abs{position:absolute}
a{color:inherit;text-decoration:none}

/* top bar */
.topbar{left:0;top:0;width:1200px;height:46px;background:var(--accent)}
.topbar__links{right:52px;top:15px;font-size:11px;word-spacing:2px}

/* hero */
.hero{left:0;top:46px;width:1200px;height:967px;
  background:
    radial-gradient(ellipse 150px 130px at 390px 230px,rgba(25,20,18,.95),rgba(25,20,18,0) 100%),
    radial-gradient(ellipse 230px 330px at 440px 560px,rgba(120,125,130,.9),rgba(120,125,130,0) 100%),
    radial-gradient(ellipse 170px 120px at 210px 590px,rgba(40,40,42,.85),rgba(40,40,42,0) 100%),
    radial-gradient(ellipse 260px 260px at 120px 170px,rgba(205,205,200,.75),rgba(205,205,200,0) 100%),
    linear-gradient(100deg,#6a6a6a 0%,#7a7a78 30%,#5a5a5a 60%,#4a4a4a 100%)}
.hero__shade{left:0;top:737px;width:1200px;height:276px;background:linear-gradient(180deg,rgba(0,0,0,.8),rgba(0,0,0,.92))}
.hero__rule{left:0;top:736px;width:1200px;height:2px;background:var(--white)}
.header__rule{left:0;top:146px;width:1200px;height:1px;background:rgba(255,255,255,.35)}

.brand{left:47px;top:82px;width:249px;height:94px;background:var(--white);clip-path:polygon(0 4%,100% 0,94% 100%,6% 96%);display:flex;align-items:center;padding-left:34px;gap:8px}
.brand__dot{width:30px;height:30px;border-radius:50%;background:var(--accent)}
.brand__name{font-size:23px;font-weight:600;color:var(--ink)}

.nav--active{left:320px;top:82px;width:91px;height:33px;background:var(--accent);font-size:11px;font-weight:600;text-transform:uppercase;display:flex;align-items:center;justify-content:center}
.nav__item{top:91px;font-size:11px;font-weight:600;text-transform:uppercase}

/* search panel */
.search{left:613px;top:148px;width:541px;height:485px;background:var(--panel)}
.search__title{left:0;top:0;width:541px;height:63px;background:var(--accent);font-size:22px;font-weight:600;display:flex;align-items:center;justify-content:center}
.search__label{right:406px;font-size:16px;color:#f2f2f2}
.search__field{left:206px;width:304px;height:32px;border:1px solid #e8e8e8;background:rgba(255,255,255,.08)}
.search__caret{right:12px;top:12px;width:0;height:0;border-left:5px solid transparent;border-right:5px solid transparent;border-top:6px solid var(--white)}
.search__btn{left:206px;top:361px;width:307px;height:41px;background:var(--accent);font-size:15px;display:flex;align-items:center;justify-content:center}
.search__tool{top:411px;width:96px;height:39px;background:#a7a7a7;color:var(--accent);display:flex;align-items:center;justify-content:center}
.search__tool--light{background:var(--white)}

/* latest jobs */
.job{width:330px;text-align:center;top:0}
.job__icon{width:126px;height:126px;border-radius:50%;background:var(--accent);border:4px solid var(--white);display:flex;align-items:center;justify-content:center;margin:674px auto 0;color:var(--accent)}
.job__title{margin-top:25px;font-size:16px;font-weight:700;color:var(--accent);letter-spacing:.5px}
.job__company{margin-top:12px;font-size:12px;line-height:16px;color:#e6e6e6}
.job__btn{display:inline-flex;align-items:center;gap:6px;margin-top:9px;width:106px;height:38px;justify-content:center;font-size:12px;border:1px solid var(--white)}
.job__btn--solid{background:var(--accent);border-color:var(--accent)}

/* article slider */
.articles{left:0;top:1013px;width:1200px;height:224px;background:var(--accent)}
.articles__photo{left:277px;top:31px;width:309px;height:166px;background:linear-gradient(120deg,#1c2a3e,#4a6c8e 55%,#c7d2dc)}
.articles__title{left:625px;top:34px;font-family:"Raleway",sans-serif;font-size:17px;font-weight:600}
.articles__text{left:625px;top:72px;width:317px;font-size:12px;line-height:17px;text-align:justify}
.articles__meta{left:625px;top:160px;display:flex;align-items:center;gap:12px;font-size:10px}
.articles__posted{background:#1f1f1f;padding:7px 8px}
.articles__comment{display:flex;align-items:center;gap:5px}
.articles__share{width:17px;height:17px;background:#1e5f88;display:inline-block;margin-right:4px;vertical-align:middle}
.articles__arrow{top:87px}

/* services */
.services{left:0;top:1237px;width:1200px;height:556px;background:linear-gradient(180deg,#2e2e2e,#454545 60%,#2c2c2c)}
.services__title{left:0;top:64px;width:1200px;text-align:center;font-family:"Raleway",sans-serif;font-size:34px;font-weight:500}
.services__title span{color:var(--accent)}
.services__intro{left:105px;top:130px;width:990px;text-align:center;font-size:12px;line-height:22px}
.app{width:343px;top:199px}
.app__tile{height:197px;background:var(--accent);display:flex;align-items:center;justify-content:center;font-size:44px;font-weight:600}
.app__label{margin-top:16px;height:33px;background:var(--white);color:var(--accent-dark);font-size:13px;font-weight:700;padding-left:12px;display:flex;align-items:center}
.app__text{margin-top:18px;font-size:12px;line-height:16px}
.app__btn{margin-top:14px;width:97px;height:35px;border:1px solid var(--white);font-size:11px;display:flex;align-items:center;justify-content:center}
.app__btn--solid{background:var(--accent);border-color:var(--accent)}

/* footer */
.footer{left:0;top:1793px;width:1200px;height:255px;background:var(--black)}
.footer__col{top:61px;font-size:11px;line-height:21px}
.footer__col h4{font-family:"Raleway",sans-serif;font-size:16px;font-weight:600;color:var(--accent);margin-bottom:10px}
.footer__col li{list-style:none}
.footer__col li::before{content:"›";margin-right:9px;font-weight:700}
.footer__divider{top:40px;width:1px;height:180px;background:#1b1b1b}
.footer__badge{left:954px;top:86px;width:166px;height:110px;background:#1c1c1c}
.footer__badge span{position:absolute;left:45px;top:28px;width:76px;height:54px;border-radius:8px;background:#5a5a5a}

.browse{left:0;top:2048px;width:1200px;height:147px;background:var(--ink);text-align:center;font-size:11px}
.browse__title{margin-top:42px;font-family:"Raleway",sans-serif;font-size:13px;font-weight:700;color:var(--accent)}
.browse__line{margin-top:7px}
.browse__line b{color:var(--accent);font-weight:400}

.bottom{left:0;top:2195px;width:1200px;height:73px;background:var(--accent);font-size:10px}
.bottom__copy{left:50px;top:32px}
.bottom__links{left:521px;top:30px}
.bottom__social{right:48px;top:30px;display:flex;gap:22px}
.bottom__social span{width:13px;height:13px;border-radius:50%;background:var(--white)}
</style>
</head>
<body>

<div class="abs topbar">
  <div class="abs topbar__links">Jobs &nbsp;| &nbsp;Career Coach &nbsp;| &nbsp;Interview Tips &nbsp;| &nbsp;Ro &nbsp;| &nbsp;En</div>
</div>

<section class="abs hero" role="img" aria-label="Photo of a young woman reading a tablet in a bright office"></section>
<div class="abs hero__shade"></div>
<div class="abs header__rule"></div>
<div class="abs hero__rule"></div>

<a class="abs brand" href="#"><span class="brand__dot"></span><span class="brand__name">LucruBrisa</span></a>
<div class="abs nav--active">Search Jobs</div>
<div class="abs nav__item" style="left:450px">My Account</div>
<div class="abs nav__item" style="left:572px">Career Counselling</div>
<div class="abs nav__item" style="left:745px">Features</div>
<div class="abs nav__item" style="left:846px">Employer &amp; Post a Job</div>
<div class="abs nav__item" style="left:1054px;top:89px">Login | Register</div>

<form class="abs search">
  <div class="abs search__title">SEARCH JOBS</div>
  <div class="abs search__label" style="top:115px">Keywords</div>
  <div class="abs search__field" style="top:110px"></div>
  <div class="abs search__label" style="top:164px">Classification</div>
  <div class="abs search__field" style="top:159px"><span class="abs search__caret"></span></div>
  <div class="abs search__label" style="top:214px">Region</div>
  <div class="abs search__field" style="top:209px"><span class="abs search__caret"></span></div>
  <div class="abs search__label" style="top:265px">Work Type</div>
  <div class="abs search__field" style="top:260px"><span class="abs search__caret"></span></div>
  <div class="abs search__label" style="top:310px">Locatie</div>
  <div class="abs search__field" style="top:305px"><span class="abs search__caret"></span></div>
  <div class="abs search__btn">SEARCH</div>
  <div class="abs search__tool" style="left:206px">
    <svg width="18" height="18" viewBox="0 0 18 18"><path d="M9 2v8M5 7l4 4 4-4" stroke="currentColor" stroke-width="2.4" fill="none"/><rect x="2" y="13" width="14" height="3" fill="currentColor"/></svg>
  </div>
  <div class="abs search__tool search__tool--light" style="left:312px">
    <svg width="18" height="18" viewBox="0 0 18 18"><path d="M3 15l5-5M8 10H4M8 10v4M15 3l-5 5M10 8h4M10 8V4" stroke="currentColor" stroke-width="2" fill="none"/></svg>
  </div>
  <div class="abs search__tool" style="left:418px">
    <svg width="16" height="18" viewBox="0 0 16 18"><path d="M2 1h8l4 4v12H2z" fill="none" stroke="currentColor" stroke-width="1.8"/><path d="M5 9h6M5 12h6" stroke="currentColor" stroke-width="1.5"/></svg>
  </div>
</form>

<article class="abs job" style="left:87px">
  <div class="job__icon">
    <svg width="46" height="46" viewBox="0 0 46 46"><path d="M14 12L4 23l10 11M32 12l10 11-10 11M26 8l-6 30" stroke="#fff" stroke-width="4" fill="none"/></svg>
  </div>
  <div class="job__title">JAVA DEVELOPER</div>
  <div class="job__company">Ulm Veltmar Engineering GmbH<br>Veltmar Engineering GmbH</div>
  <a class="job__btn job__btn--solid" href="#">Read More <span>▸</span></a>
</article>
<article class="abs job" style="left:445px">
  <div class="job__icon">
    <svg width="46" height="46" viewBox="0 0 46 46"><circle cx="23" cy="14" r="9" fill="#fff"/><path d="M6 42c0-11 8-17 17-17s17 6 17 17z" fill="#fff"/></svg>
  </div>
  <div class="job__title">JR. DEVELOPER</div>
  <div class="job__company">Atlanta, GA Corvane Network Solutions, Inc<br>Corvane Network Solutions, Inc</div>
  <a class="job__btn" href="#">Read More <span>▸</span></a>
</article>
<article class="abs job" style="left:767px">
  <div class="job__icon">
    <svg width="40" height="46" viewBox="0 0 40 46"><rect x="4" y="2" width="32" height="42" fill="#fff"/><g fill="currentColor"><rect x="9" y="7" width="5" height="5"/><rect x="17.5" y="7" width="5" height="5"/><rect x="26" y="7" width="5" height="5"/><rect x="9" y="16" width="5" height="5"/><rect x="17.5" y="16" width="5" height="5"/><rect x="26" y="16" width="5" height="5"/><rect x="9" y="25" width="5" height="5"/><rect x="17.5" y="25" width="5" height="5"/><rect x="26" y="25" width="5" height="5"/><rect x="16" y="34" width="8" height="10"/></g></svg>
  </div>
  <div class="job__title">DIGITAL PROJECT MANAGER</div>
  <div class="job__company">Amsterdam Harlow Bond Ltd<br>Harlow Bond Ltd</div>
  <a class="job__btn" href="#">Read More <span>▸</span></a>
</article>

<section class="abs articles">
  <svg class="abs articles__arrow" style="left:106px" width="38" height="40" viewBox="0 0 38 40"><path d="M0 20L38 0 28 20 38 40z" fill="#fff"/></svg>
  <div class="abs articles__photo" role="img" aria-label="Photo of a woman using a tablet in front of a city skyline at night"></div>
  <h3 class="abs articles__title">Invatarea, Continua pe tot Parcursul Vietii</h3>
  <p class="abs articles__text">Lorem ipsum dolor sit amet, consectetur adipiscing elit, sed do eiusmod tempor incididunt ut labore et dolore magna aliqua.Lorem ipsum dolor sit amet, consectetur adipiscing elit, sed do eiusmod tempor incididunt</p>
  <div class="abs articles__meta">
    <span class="articles__posted">Posted by : 20-Aug-2015</span>
    <span class="articles__comment"><svg width="12" height="10" viewBox="0 0 12 10"><path d="M1 1h10v6H5L2 9V7H1z" fill="#f5c518"/></svg>Comment : 3</span>
    <span><i class="articles__share"></i><i class="articles__share"></i><i class="articles__share"></i></span>
  </div>
  <svg class="abs articles__arrow" style="left:1050px" width="38" height="40" viewBox="0 0 38 40"><path d="M38 20L0 0l10 20L0 40z" fill="#fff"/></svg>
</section>

<section class="abs services" role="img" aria-label="Dim background photo of office chairs"></section>
<section class="abs services" style="background:none">
  <h2 class="abs services__title">Our <span>Service</span></h2>
  <p class="abs services__intro">Lorem ipsum dolor sit amet, consectetur adipiscing elit, sed do eiusmod tempor incididunt ut labore et dolore magna aliqua. Ut enim ad minim veniam, quis nostrud exercitation ullam-co laboris. Duis aute irure dolor in reprehenderit in voluptate velit esse cillum dolore eu fugiat nulla pariatur.</p>

  <div class="abs app" style="left:49px">
    <div class="app__tile">Pomelo</div>
    <div class="app__label">JOB APP FOR POMELO</div>
    <p class="app__text">Lorem ipsum dolor sit amet, consectetur adipiscing elit, sed do eiusmod tempor incididunt</p>
    <a class="app__btn app__btn--solid" href="#">READ MORE</a>
  </div>
  <div class="abs app" style="left:433px">
    <div class="app__tile">Robodroid</div>
    <div class="app__label">JOB APP FOR ROBODROID</div>
    <p class="app__text">Lorem ipsum dolor sit amet, consectetur adipiscing elit, sed do eiusmod tempor incididunt</p>
    <a class="app__btn" href="#">READ MORE</a>
  </div>
  <div class="abs app" style="left:811px">
    <div class="app__tile">Friendbook</div>
    <div class="app__label">JOB APP FOR FRIENDBOOK</div>
    <p class="app__text">Lorem ipsum dolor sit amet, consectetur adipiscing elit, sed do eiusmod tempor incididunt</p>
    <a class="app__btn" href="#">READ MORE</a>
  </div>
</section>

<footer class="abs footer">
  <div class="abs footer__col" style="left:47px"><h4>Connect with us</h4><ul><li>Friendbook</li><li>Chirper</li><li>Circles+</li><li>ProLink</li><li>Blog</li></ul></div>
  <div class="abs footer__divider" style="left:225px"></div>
  <div class="abs footer__col" style="left:260px"><h4>Go Mobile</h4><ul><li>Pomelo App</li><li>Robodroid App</li><li>Friendbook App</li><li>Mobile Version</li></ul></div>
  <div class="abs footer__divider" style="left:458px"></div>
  <div class="abs footer__col" style="left:491px"><h4>Employer Tools</h4><ul><li>Post job ads</li><li>Access jobseekers</li><li>Resume Search</li><li>Analytics</li></ul></div>
  <div class="abs footer__divider" style="left:696px"></div>
  <div class="abs footer__col" style="left:729px"><h4>Job Seeker Tools</h4><ul><li>Resume Posting</li><li>Job Alerts</li><li>Video Resume</li><li>Create Profile</li></ul></div>
  <div class="abs footer__divider" style="left:932px"></div>
  <div class="abs footer__col" style="left:978px"><h4>Our Partners</h4></div>
  <div class="abs footer__badge"><span></span></div>
</footer>

<section class="abs browse">
  <div class="browse__title">Browse Jobs By</div>
  <div class="browse__line"><b>Classifications:</b> IT_Software Development | Banking | Sales | Medical | Engineering | view all classifications</div>
  <div class="browse__line"><b>Cities:</b> Bucuresti | Cluj-Napoca | Timisoara | Iasi | Constanta | Craiova | Brasov | Galati | Ploiesti | Oradea | Pitesti | Sibiu</div>
</section>

<div class="abs bottom">
  <div class="abs bottom__copy">© All Rights Reserved. Copyrights @lucrubrisa. 2015</div>
  <div class="abs bottom__links">About us | Terms and conditions | Privacy Policy | Contact</div>
  <div class="abs bottom__social"><span></span><span></span><span></span><span></span><span></span></div>
</div>

</body>
</html>
```